West Texas Craft Vodka

Looking for imagery, name and logo for a West Texas Craft vodka. Needs to have a feel and look of West Texas – Rustic feel in look / name. Please submit with Bottle Image with entry...looking for the actual bottle with graphics. Looking for creative name as well for this vodka

```html
<!DOCTYPE html>
<html lang="en">
<head>
<meta charset="utf-8">
<title>Rusty Spur Craft Vodka Label and Bottle</title>
<link href="https://fonts.googleapis.com/css2?family=Anton&family=Barlow:wght@400;500&display=swap" rel="stylesheet">
<style>
  :root {
    --paper: #ffffff;
    --brand-red: #9b1d22;
    --flag-blue: #2b3d56;
    --flag-cream: #d9d2bd;
    --flag-red: #b42a2a;
    --band-blue: #2f5672;
    --band-text: #ffffff;
    --wire-grey: #8a8a8a;
    --glass-light: #eef1f3;
    --glass-mid: #cfd5da;
    --glass-dark: #9aa3ab;
    --cap: #2a2a2a;
  }
  * { margin: 0; padding: 0; box-sizing: border-box; }
  html, body {
    width: 1200px;
    height: 1091px;
    overflow: hidden;
    background: var(--paper);
  }
  .canvas {
    position: relative;
    width: 1200px;
    height: 1091px;
    background: var(--paper);
  }

  /* Bottle presentation */
  .bottle {
    position: absolute;
    left: 20px;
    top: 50px;
    width: 344px;
    height: 960px;
  }
  .bottle-glass {
    position: absolute;
    inset: 0;
    width: 344px;
    height: 960px;
  }
  .bottle-label {
    position: absolute;
    left: 13px;
    top: 437px;
    width: 318px;
    height: 430px;
    background: var(--paper);
  }
  .bottle-label .brand-name {
    position: absolute;
    top: 22px;
    left: 0;
    width: 318px;
    text-align: center;
    font-family: "Anton", Impact, sans-serif;
    font-size: 46px;
    line-height: 1;
    letter-spacing: 3px;
    color: var(--brand-red);
  }
  .bottle-label .flag-art {
    position: absolute;
    top: 89px;
    left: 0;
    width: 318px;
    height: 208px;
  }
  .bottle-label .product-type {
    position: absolute;
    top: 313px;
    left: 0;
    width: 318px;
    text-align: center;
    font-family: "Anton", Impact, sans-serif;
    font-size: 32px;
    line-height: 1;
    letter-spacing: 2px;
    color: var(--brand-red);
  }
  .bottle-label .details-band {
    position: absolute;
    top: 356px;
    left: 0;
    width: 318px;
    height: 52px;
    background: var(--band-blue);
    color: var(--band-text);
    font-family: "Barlow", Arial, sans-serif;
    text-align: center;
    padding-top: 3px;
  }
  .bottle-label .origin { font-size: 13px; line-height: 17px; }
  .bottle-label .abv { font-size: 9px; line-height: 13px; }
  .bottle-label .volume { font-size: 11px; line-height: 14px; }
  .bottle-label .wire { width: 318px; top: 414px; }

  /* Flat label */
  .label {
    position: absolute;
    left: 396px;
    top: 58px;
    width: 760px;
    height: 980px;
  }
  .wire {
    position: absolute;
    left: 0;
    width: 760px;
    height: 16px;
    background: linear-gradient(180deg, transparent 6px, var(--wire-grey) 6px, var(--wire-grey) 10px, transparent 10px);
  }
  .label .wire--top { top: 0; }
  .label .wire--bottom { top: 964px; }
  .label .brand-name {
    position: absolute;
    top: 36px;
    left: 0;
    width: 760px;
    text-align: center;
    font-family: "Anton", Impact, sans-serif;
    font-size: 118px;
    line-height: 1.05;
    letter-spacing: 10px;
    color: var(--brand-red);
  }
  .flag-art {
    background: linear-gradient(100deg, var(--flag-blue) 0%, var(--flag-blue) 26%, var(--flag-cream) 48%, var(--flag-red) 85%);
  }
  .label .flag-art {
    position: absolute;
    top: 195px;
    left: 0;
    width: 760px;
    height: 491px;
  }
  .label .product-type {
    position: absolute;
    top: 718px;
    left: 0;
    width: 760px;
    text-align: center;
    font-family: "Anton", Impact, sans-serif;
    font-size: 78px;
    line-height: 1.05;
    letter-spacing: 6px;
    color: var(--brand-red);
  }
  .label .details-band {
    position: absolute;
    top: 833px;
    left: 0;
    width: 760px;
    height: 118px;
    background: var(--band-blue);
    color: var(--band-text);
    font-family: "Barlow", Arial, sans-serif;
    text-align: center;
    padding-top: 8px;
  }
  .label .origin { font-size: 28px; font-weight: 500; line-height: 38px; }
  .label .abv { font-size: 19px; line-height: 34px; }
  .label .volume { font-size: 23px; line-height: 30px; }
</style>
</head>
<body>
  <main class="canvas">
    <section class="bottle">
      <svg class="bottle-glass" viewBox="0 0 344 960" role="img" aria-label="Clear glass vodka bottle with black screw cap">
        <defs>
          <linearGradient id="glass" x1="0" x2="1" y1="0" y2="0">
            <stop offset="0" stop-color="var(--glass-dark)"/>
            <stop offset="0.25" stop-color="var(--glass-light)"/>
            <stop offset="0.7" stop-color="var(--glass-mid)"/>
            <stop offset="1" stop-color="var(--glass-dark)"/>
          </linearGradient>
        </defs>
        <path d="M118 70 L118 105 Q118 200 40 250 Q4 275 4 330 L4 920 Q4 958 40 958 L304 958 Q340 958 340 920 L340 330 Q340 275 304 250 Q226 200 226 105 L226 70 Z" fill="url(#glass)"/>
        <rect x="102" y="2" width="140" height="72" rx="8" fill="var(--cap)"/>
      </svg>
      <div class="bottle-label">
        <h2 class="brand-name">RUSTY SPUR</h2>
        <div class="flag-art" role="img" aria-label="Weathered Texas flag with the state outline drawn in barbed wire"></div>
        <p class="product-type">CRAFT VODKA</p>
        <div class="details-band">
          <p class="origin">Distilled In West Texas</p>
          <p class="abv">Alc. 40% By Vol</p>
          <p class="volume">750ml</p>
        </div>
        <div class="wire" role="img" aria-label="Barbed wire border"></div>
      </div>
    </section>

    <section class="label">
      <div class="wire wire--top" role="img" aria-label="Barbed wire border"></div>
      <h1 class="brand-name">RUSTY SPUR</h1>
      <div class="flag-art" role="img" aria-label="Weathered Texas flag with the state outline drawn in barbed wire"></div>
      <h2 class="product-type">CRAFT VODKA</h2>
      <div class="details-band">
        <p class="origin">Distilled In West Texas</p>
        <p class="abv">Alc. 40% By Vol</p>
        <p class="volume">750ml</p>
      </div>
      <div class="wire wire--bottom" role="img" aria-label="Barbed wire border"></div>
    </section>
  </main>
</body>
</html>
```